Design 2 8x10 one page sales brochures for TELNIQ, a cloud service provider.

We’re open to fun and creative, yet must be clean, bold and professional.

***The winning designer will also be hired to design a handful of other brochures for us after the contest***

We understand the value of feedback and will work closely with every design to create the perfect sales brochure!

Should be printer friendly, primarily white so doesn’t consume a lot of printer ink
Colors - grey, black, light blue, llight green
We are a fun, easy to work with technology company and the brochures need to reflect taht.

Don't hesitate to ask any questions, thanks!

We need two designs, each one page 8x10"
#1 Why we're Zip
#2 TELNIQTalk

Target Market(s)

Small and medium sized business owners

Industry/Entity Type

Telecommunications

Font styles to use
Sans Serif

Requirements
Must have
• Clean, professional designs. We're a fun tech company.
• Visually appealing
Nice to have
• graphs, charts, diagrams, etc
Should not have
• not sure.

```html
<!DOCTYPE html>
<html lang="en">
<head>
<meta charset="utf-8">
<title>TELNIQ Sales Brochures</title>
<link href="https://fonts.googleapis.com/css2?family=Source+Sans+3:wght@300;400;600;700&display=swap" rel="stylesheet">
<style>
:root{
  --stage:#a9a9a9;
  --paper:#ffffff;
  --ink:#231f20;
  --body:#4d4d4f;
  --blue:#1a9ad6;
  --sky:#29a8e0;
  --teal:#5cc6bd;
  --mint:#4fc4b4;
  --mist:#f1f2f5;
  --rule:#c9c9cb;
  --black:#050505;
}
*{margin:0;padding:0;box-sizing:border-box}
html,body{width:1200px;height:862px;overflow:hidden}
body{background:var(--stage);font-family:"Source Sans 3",sans-serif;color:var(--ink);position:relative}
.sheet{position:absolute;top:95px;width:520px;height:652px;background:var(--paper);overflow:hidden;box-shadow:0 14px 18px -8px rgba(0,0,0,.35)}
.sheet--front{left:58px}
.sheet--back{left:617px;top:96px}
.accent{color:var(--blue)}

/* front */
.photo{position:absolute;left:0;top:60px;width:520px;height:365px;background:linear-gradient(100deg,#dfe6e2 0%,#f4f6f5 40%,#eceef0 60%,#b9bdbf 100%)}
.header-shape{position:absolute;left:0;top:0;width:520px;height:140px}
.photo-edge{position:absolute;left:0;top:360px;width:520px;height:70px}
.brand{position:absolute;left:32px;top:26px;display:flex;align-items:center;gap:8px}
.brand__dot{width:22px;height:22px;border-radius:50%;background:var(--blue)}
.brand__name{font-size:25px;font-weight:700;color:var(--blue);letter-spacing:.5px}
.tagline{position:absolute;right:34px;top:33px;text-align:right;font-size:12.5px;line-height:14px;font-weight:300;color:#fff}
.tagline span{color:var(--sky);font-weight:400}
.headline{position:absolute;right:34px;top:140px;text-align:right;font-size:17px;line-height:19.5px;font-weight:600;color:var(--ink)}
.pitch{position:absolute;left:0;width:520px;top:412px;text-align:center;font-size:19px;font-weight:600}
.pitch span{color:var(--mint);font-weight:700}
.perks{position:absolute;left:14px;top:454px;width:492px;display:flex}
.perk{flex:1;text-align:center;font-size:12px;line-height:14.5px;color:var(--body);font-weight:400;border-right:1px solid var(--rule);height:88px;padding-top:2px}
.perk:last-child{border-right:none}
.perk svg{display:block;margin:0 auto 6px}
.band-teal{position:absolute;left:0;top:565px;width:520px;height:45px;background:var(--teal);color:#fff;font-size:10.5px;line-height:13px;text-align:center;padding:10px 60px 0;font-weight:300}
.band-contact{position:absolute;left:0;top:610px;width:520px;height:42px;background:var(--sky);color:#fff;text-align:center;font-size:9.8px;font-weight:300;padding-top:7px}
.band-contact__row{display:flex;justify-content:center;gap:30px;margin-top:4px}
.band-contact__row span{display:flex;align-items:center;gap:6px}

/* back */
.intro{position:absolute;left:39px;top:36px;width:440px}
.intro h2{font-size:18px;font-weight:700;color:var(--blue);line-height:20px}
.intro p{font-size:9.6px;line-height:12px;color:var(--body)}
.experience{position:absolute;left:39px;top:110px;width:450px;font-size:9.6px;line-height:12px;color:var(--body)}
.experience b{color:var(--blue);font-weight:400;font-size:12px}
.sds-title{position:absolute;left:40px;top:170px;font-size:18px;font-weight:400}
.features{position:absolute;left:41px;top:206px;width:450px;list-style:none}
.feature{display:flex;gap:14px;margin-bottom:8px}
.feature svg{flex:none;margin-top:1px}
.feature h3{font-size:9.6px;font-weight:600;color:var(--blue);line-height:12px}
.feature p{font-size:9.6px;line-height:12px;color:var(--ink)}
.cloud-zone{position:absolute;left:0;top:405px;width:520px;height:205px}
.closing{position:absolute;left:39px;top:467px;width:470px;font-size:14.5px;line-height:17.5px;font-weight:300;color:#444;white-space:nowrap}
.closing b{color:var(--blue);font-weight:400}
.lineup-lead{position:absolute;left:39px;top:512px;font-size:10px;color:var(--body)}
.lineup{position:absolute;top:537px;list-style:none;font-size:10.5px;line-height:13px;color:var(--body)}
.lineup--a{left:58px}
.lineup--b{left:268px}
.lineup b{color:var(--blue);font-weight:400}
.signoff{position:absolute;left:400px;top:558px;display:flex;align-items:center;gap:6px}
.signoff__dot{width:14px;height:14px;border-radius:50%;background:var(--blue)}
.signoff__name{font-size:17px;font-weight:700;color:var(--blue)}
</style>
</head>
<body>

<section class="sheet sheet--front">
  <div class="photo" role="img" aria-label="Office desk with a black VoIP desk phone, coiled cord, pen cup and green plants"></div>
  <svg class="header-shape" viewBox="0 0 520 140" aria-hidden="true">
    <path d="M0 0H520V110Q490 100 455 118Q430 70 380 72Q320 70 290 98Q270 72 225 78Q175 78 150 100Q110 88 60 102Q25 108 0 125Z" fill="var(--black)"/>
    <path d="M520 110Q490 100 455 118Q430 70 380 72Q320 70 290 98Q270 72 225 78Q175 78 150 100Q110 88 60 102Q25 108 0 125" fill="none" stroke="var(--sky)" stroke-width="3"/>
  </svg>
  <svg class="photo-edge" viewBox="0 0 520 70" aria-hidden="true">
    <path d="M0 70V52Q30 30 90 40Q140 5 220 22Q260 0 320 18Q380 8 420 30Q480 20 520 40V70Z" fill="var(--paper)"/>
  </svg>

  <div class="brand"><span class="brand__dot"></span><span class="brand__name">TELNIQ</span></div>
  <p class="tagline">YOUR PHONE SYSTEM DOESN’T<br><span>HAVE TO BE LAME.</span></p>
  <h1 class="headline"><span class="accent">TELNIQ</span>’s radical hosted VOiP solution<br><span class="accent">TELNIQTalk</span> is setting the new standard<br>for enterprise grade voice</h1>

  <h2 class="pitch">What puts the Zip in TELNIQ, <span>SIMPLICITY.</span></h2>
  <div class="perks">
    <div class="perk">
      <svg width="38" height="38" viewBox="0 0 38 38"><circle cx="19" cy="19" r="16.5" fill="none" stroke="var(--sky)" stroke-width="2.5"/><rect x="13" y="10" width="12" height="16" fill="none" stroke="var(--sky)" stroke-width="1.8"/><path d="M15 15h8M15 19h8M15 23h5" stroke="var(--sky)" stroke-width="1.5"/><path d="M8 30L30 8" stroke="var(--sky)" stroke-width="2.5"/></svg>
      No contracts</div>
    <div class="perk">
      <svg width="38" height="38" viewBox="0 0 38 38"><circle cx="19" cy="19" r="16.5" fill="none" stroke="var(--sky)" stroke-width="2.5"/><text x="19" y="27" text-anchor="middle" font-size="24" font-weight="700" fill="none" stroke="var(--sky)" stroke-width="1.6" font-family="Source Sans 3,sans-serif">$</text><path d="M8 30L30 8" stroke="var(--sky)" stroke-width="2.5"/></svg>
      No upfront costs<br>or hidden fees</div>
    <div class="perk">
      <svg width="38" height="38" viewBox="0 0 38 38"><circle cx="19" cy="19" r="16.5" fill="none" stroke="var(--sky)" stroke-width="2.5"/><rect x="10" y="12" width="18" height="11" fill="none" stroke="var(--sky)" stroke-width="1.8"/><path d="M8 26h22" stroke="var(--sky)" stroke-width="2"/><path d="M13 20l4-4 3 3 4-4" fill="none" stroke="var(--sky)" stroke-width="1.4"/></svg>
      Free<br>installation</div>
    <div class="perk">
      <svg width="38" height="38" viewBox="0 0 38 38"><circle cx="19" cy="19" r="16.5" fill="none" stroke="var(--sky)" stroke-width="2.5"/><circle cx="19" cy="19" r="6" fill="none" stroke="var(--sky)" stroke-width="3" stroke-dasharray="3 2"/><circle cx="19" cy="19" r="2.2" fill="var(--sky)"/></svg>
      Free lifetime<br>training<br>&amp; support</div>
  </div>

  <p class="band-teal">Radically simple customization - the flexibility to choose between hundreds of custom features and products.</p>
  <div class="band-contact">
    We know you’re tired of your lame phone system, contact TELNIQ today and make it radical!
    <div class="band-contact__row">
      <span><svg width="10" height="10" viewBox="0 0 10 10"><path d="M2 1l2 2-1 1.5q1 2 2.5 2.5L7 6l2 2-1.5 1.5Q3 9 .5 2.5Z" fill="#fff"/></svg>555-014-2290</span>
      <span><svg width="11" height="8" viewBox="0 0 11 8"><rect x=".5" y=".5" width="10" height="7" fill="none" stroke="#fff"/><path d="M.5.5l5 4 5-4" fill="none" stroke="#fff"/></svg>sales@telniq.com</span>
      <span><svg width="10" height="10" viewBox="0 0 10 10"><circle cx="5" cy="5" r="4.3" fill="none" stroke="#fff"/><path d="M.7 5h8.6M5 .7q-3 4.3 0 8.6q3-4.3 0-8.6" fill="none" stroke="#fff" stroke-width=".8"/></svg>www.telniq.com</span>
    </div>
  </div>
</section>

<section class="sheet sheet--back">
  <div class="intro">
    <h2>Radically Simple Cloud</h2>
    <p>TELNIQ delivers customized cloud solutions to enterprises and small businesses<br>&nbsp;with the highest level of value, integrity, service, and support - radically changing<br>your ability to communicate and compete in the market</p>
  </div>
  <p class="experience"><b>100+ years</b> of collective experience activating over 1M user seats, working with some of the largest organizations in the world. We leveraged our experiences to build an innovative suite of cloud offerings and features, allowing us to build custom solutions based on unique and changing customer needs.</p>

  <h2 class="sds-title">Super Duper Simple (SDS)</h2>
  <ul class="features">
    <li class="feature"><svg width="22" height="22" viewBox="0 0 22 22"><path d="M3 19L19 3M3 3l16 16" stroke="var(--blue)" stroke-width="2.4"/></svg><div><h3>Set-up:</h3><p>Simple user discovery process, custom provisioning to your needs</p></div></li>
    <li class="feature"><svg width="22" height="22" viewBox="0 0 22 22"><rect x="3" y="4" width="16" height="11" fill="none" stroke="var(--blue)" stroke-width="1.6"/><path d="M1 18h20" stroke="var(--blue)" stroke-width="2"/></svg><div><h3>Installation:</h3><p>Virtually plug &amp; play, your custom configuration up and running in minutes</p></div></li>
    <li class="feature"><svg width="22" height="22" viewBox="0 0 22 22"><rect x="8" y="3" width="12" height="9" fill="none" stroke="var(--blue)" stroke-width="1.6"/><rect x="3" y="9" width="4" height="11" fill="var(--blue)"/></svg><div><h3>Training:</h3><p>Simple, intuitive training to allow you to focus on your business. On the web, over the<br>phone, or in person</p></div></li>
    <li class="feature"><svg width="22" height="22" viewBox="0 0 22 22"><g fill="var(--blue)"><circle cx="5" cy="6" r="2.5"/><circle cx="11" cy="6" r="2.5"/><circle cx="17" cy="6" r="2.5"/><rect x="2" y="10" width="18" height="3" rx="1.5"/><circle cx="5" cy="15" r="2"/><circle cx="11" cy="15" r="2"/><circle cx="17" cy="15" r="2"/><rect x="2" y="18" width="18" height="3" rx="1.5"/></g></svg><div><h3>Management:</h3><p>Access and manage from any web enabled device, tablet, or P.</p></div></li>
    <li class="feature"><svg width="22" height="22" viewBox="0 0 22 22"><circle cx="11" cy="11" r="8.5" fill="none" stroke="var(--blue)" stroke-width="2"/><path d="M4 12v-2M18 12v-2" stroke="var(--blue)" stroke-width="3"/></svg><div><h3>Support:</h3><p>Support that matches your business needs 24/7/365. We take care of our customers.<br>Plain and simple.</p></div></li>
    <li class="feature"><svg width="22" height="22" viewBox="0 0 22 22"><path d="M4 18L18 4M11 4h7v7M4 11v7h7" fill="none" stroke="var(--blue)" stroke-width="1.6"/></svg><div><h3>Scalability</h3><p>Add users and features to grow with your business</p></div></li>
  </ul>

  <svg class="cloud-zone" viewBox="0 0 520 205" aria-hidden="true">
    <path d="M0 58Q40 30 95 22Q140 0 200 20Q215 28 225 26Q270 -5 330 8Q390 20 431 55Q470 35 520 33V205H0Z" fill="var(--mist)"/>
    <path d="M0 58Q40 30 95 22Q140 0 200 20Q215 28 225 26Q270 -5 330 8Q390 20 431 55Q470 35 520 33" fill="none" stroke="#8ea7cc" stroke-width="1"/>
  </svg>
  <p class="closing">Make your business’s communications not lame system phone<br>system not lame with <b>TELNIQTalk</b>: a radically simple way to communicate!</p>
  <p class="lineup-lead"><span class="accent">TELNIQ</span>’s radical cloud solutions are setting the new standard for enterprise grade cloud:</p>
  <ul class="lineup lineup--a">
    <li><b>TELNIQ</b>Talk</li>
    <li><b>ZIP</b>CallCenter</li>
    <li><b>ZIP</b>Meetings</li>
    <li><b>ZIP</b>Apps (mobile, desktop, web)</li>
  </ul>
  <ul class="lineup lineup--b">
    <li>Simply<b>ZIP</b></li>
    <li>Super<b>ZIP</b></li>
    <li>Ultra<b>ZIP</b></li>
  </ul>
  <div class="signoff"><span class="signoff__dot"></span><span class="signoff__name">TELNIQ</span></div>

  <div class="band-contact">
    We know you’re tired of your lame phone system, contact TELNIQ today and make it radical!
    <div class="band-contact__row">
      <span><svg width="10" height="10" viewBox="0 0 10 10"><path d="M2 1l2 2-1 1.5q1 2 2.5 2.5L7 6l2 2-1.5 1.5Q3 9 .5 2.5Z" fill="#fff"/></svg>555-014-2290</span>
      <span><svg width="11" height="8" viewBox="0 0 11 8"><rect x=".5" y=".5" width="10" height="7" fill="none" stroke="#fff"/><path d="M.5.5l5 4 5-4" fill="none" stroke="#fff"/></svg>sales@telniq.com</span>
      <span><svg width="10" height="10" viewBox="0 0 10 10"><circle cx="5" cy="5" r="4.3" fill="none" stroke="#fff"/><path d="M.7 5h8.6M5 .7q-3 4.3 0 8.6q3-4.3 0-8.6" fill="none" stroke="#fff" stroke-width=".8"/></svg>www.telniq.com</span>
    </div>
  </div>
</section>

</body>
</html>
```